Realty Group Needs Classy, Contemporary Letterhead Design

We need a letterhead design for a new realty company located in NY, USA. We buy investment properties to rehabilitate and or keep in our rental portfolio.

```html
<!DOCTYPE html>
<html lang="en">
<head>
<meta charset="UTF-8">
<title>Meridian Realty Group Letterhead</title>
<link href="https://fonts.googleapis.com/css2?family=Open+Sans:wght@400;600;700&display=swap" rel="stylesheet">
<style>
  :root {
    --brand: #4a2a86;
    --ink: #222222;
    --muted: #5a5a5a;
    --paper: #ffffff;
  }
  * { margin: 0; padding: 0; box-sizing: border-box; }
  html, body { width: 1029px; height: 1200px; overflow: hidden; background: var(--paper); }
  body { font-family: "Open Sans", Arial, sans-serif; color: var(--ink); }
  .letterhead { position: relative; width: 1029px; height: 1200px; }

  .brand { position: absolute; left: 69px; top: 62px; display: flex; align-items: center; gap: 10px; }
  .brand-mark { width: 16px; height: 16px; border-radius: 50%; background: var(--brand); }
  .brand-name { font-size: 26px; font-weight: 700; color: var(--brand); letter-spacing: 0.5px; }

  .meta { position: absolute; left: 69px; top: 242px; font-size: 13.5px; color: var(--ink); line-height: 28px; }
  .date { position: absolute; right: 69px; top: 240px; font-size: 15.5px; color: var(--muted); }

  .body-copy { position: absolute; left: 69px; right: 62px; top: 326px; font-size: 15.8px; line-height: 24.3px; }
  .salutation { margin-bottom: 14px; color: var(--muted); }
  .body-copy p.para { margin-bottom: 24px; }

  .signoff { position: absolute; left: 69px; top: 793px; font-size: 15.8px; line-height: 24.3px; }
  .signoff .closing { margin-bottom: 24px; }
  .signoff .signer { color: #000; }

  .footer { position: absolute; left: 69px; top: 1138px; display: flex; font-size: 14px; line-height: 20px; color: var(--muted); }
  .contact { width: 234px; }
  .contact .label { color: var(--brand); display: inline-block; width: 14px; font-weight: 600; font-size: 12px; }
  .address { width: 250px; }
  .website { align-self: flex-end; color: var(--brand); }
</style>
</head>
<body>
<div class="letterhead">
  <header class="brand">
    <span class="brand-mark"></span>
    <span class="brand-name">Meridian Realty Group, LLC</span>
  </header>

  <div class="meta">
    <div>Re:</div>
    <div>To:</div>
  </div>
  <div class="date">December 29, 2021</div>

  <main class="body-copy">
    <p class="salutation">Dear Thomas,</p>
    <p class="para">Lorem ipsum dolor sit amet, consectetur adipiscing elit. Donec orci purus, luctus vitae dignissim eu, iaculis sed purus. Vivamus faucibus, ipsum nec aliquet viverra, leo mauris condimentum ligula, sit amet sagittis enim ligula quis arcu. Nam egestas tortor id nisi porttitor mattis. In tortor ante, ultricies in suscipit a, tempus non massa. Vivamus et auctor mi. Fusce vel massa nulla. Phasellus nec eros mauris, et scelerisque orci.</p>
    <p class="para">Donec malesuada orci vitae nulla accumsan porta a id massa. Quisque accumsan iaculis magna sit amet fringilla. Maecenas consequat, magna eget tincidunt semper, odio nibh rutrum mi, id feugiat ante nisi eu risus. Vestibulum nunc orci, rhoncus a placerat in, ultricies in mi. Cras mattis varius eros, vel fringilla nisi suscipit eget. Quisque scelerisque sagittis nulla at porttitor.</p>
    <p class="para">Sed id augue vitae urna euismod commodo aliquet a quam. Pellentesque arcu velit, cursus et malesuada ut, consequat et diam. Nullam erat sem, rhoncus id ullamcorper vitae, rhoncus et arcu. In ultricies ultricies nulla, ut rutrum nisi iaculis at. Donec eu magna a metus ornare faucibus. Fusce aliquet faucibus ultricies. Morbi semper, est id tincidunt gravida, sem arcu adipiscing lacus, ac bibendum nulla leo eu purus. Quisque nec diam sed risus consectetur a ccumsan quis quis nibh. Vestibulum id purus lorem.</p>
  </main>

  <section class="signoff">
    <p class="closing">Sincerily,</p>
    <p class="signer">Daniel Reyes</p>
    <p>General Manager</p>
  </section>

  <footer class="footer">
    <div class="contact">
      <div><span class="label">p</span>(555) 014-2280</div>
      <div><span class="label">e</span>info@meridianrealtygroup.com</div>
    </div>
    <div class="address">
      <div>2870 Larkspur Drive,</div>
      <div>Suite 1, Meridian Realty Group</div>
    </div>
    <div class="website">www.meridianrealtygroup.com</div>
  </footer>
</div>
</body>
</html>
```